Feedback App to request feedback from colleagues

It’s a small web app to collect feedback from team members. This is the general screen flow but happy for variations to it.

Users logs into application and is able to see the feedback received till date from different colleagues.

At the top right are “Request feedback”, “Respond to Feedback”.

When the user clicks on Request Feedback, there are three options.
Adhoc Feedback
Mid Year Feedback
360 Feedback

Adhoc feedback will open a screen where I can search for colleagues to request feedback from (I can select more than one). There are three pre-defined question that can I edit if needed.

Mid year feedback: same process but questions cannot be edited

360 Feedback - just redirect to another website.

Respond to Feedback - see incoming request and the ability to provide feedback to questions received.

Send Feedback: select a colleague and send adhoc feedback.

Colours to be used are white and red only. Simple design, the app will be embedded in a portal so need for headers etc. think of a mobile view but no need for logo, header bar etc

Colour Codes:
Red: #E60000
White #FFFFFF
Grey: #333333 (Only use if needed e.g. borders, background etc)
Black: #000000

Only the above colours to be used

Number of Pages Required

1 page

Font styles to use
Sans Serif

Colors
EB3D1F
EC4F4E
F09395
F8D3D4
FCEDEE

Requirements
Must have
• Design screens for every page mentioned
Nice to have
• Clean design, use of images and icons
Should not have
• Cluttered design, header

```html
<!DOCTYPE html>
<html lang="en">
<head>
<meta charset="utf-8">
<title>Feedback App Screens</title>
<link href="https://fonts.googleapis.com/css2?family=Roboto:ital,wght@0,400;0,500;1,400;1,500&display=swap" rel="stylesheet">
<style>
:root{
  --red:#EC4F4E;
  --red-deep:#E8453F;
  --ink:#222222;
  --text:#333333;
  --white:#FFFFFF;
  --blush-top:#FCEAE8;
  --blush-bottom:#F9CFC4;
  --footer-band:#F9C6BA;
  --field:#FCE3E1;
  --muted:#B9B2B2;
}
*{box-sizing:border-box;margin:0;padding:0}
html,body{width:1200px;height:1200px;overflow:hidden;background:var(--white)}
body{position:relative;font-family:'Roboto',Arial,sans-serif;color:var(--text)}
.screen{position:absolute;width:240px;height:428px;overflow:hidden;background:linear-gradient(180deg,var(--blush-top) 0%,var(--blush-bottom) 100%);box-shadow:0 2px 8px rgba(0,0,0,.06)}
.status-bar{position:absolute;left:0;top:0;width:100%;height:17px;background:var(--ink);color:var(--white);font-size:8px;line-height:17px;padding-left:9px}
.status-icons{position:absolute;right:9px;top:4px}
.app-bar{position:absolute;left:0;top:17px;width:100%;height:28px;background:var(--red);color:var(--white);font-size:10px;font-weight:500;line-height:28px;text-align:center}
.app-bar.left-title{text-align:left;padding-left:9px}
.app-bar .nav-back{position:absolute;left:8px;top:9px}
.app-bar .nav-action{position:absolute;right:9px;top:8px}
.illustration{position:absolute;border-radius:50%}
.btn{position:absolute;height:25px}
.btn::before{content:"";position:absolute;left:-4px;top:-3px;width:60%;height:100%;background:var(--white);transform:skewX(-8deg)}
.btn .face{position:absolute;inset:0;background:var(--red);transform:skewX(-8deg);box-shadow:0 2px 4px rgba(200,60,60,.25)}
.btn.right::before{left:auto;right:-4px;top:-3px}
.btn.dark .face{background:#111111}
.btn .label{position:absolute;inset:0;color:var(--white);font-size:10px;font-weight:500;line-height:25px;text-align:center}
.btn.wide{height:29px}
.btn.wide .label{line-height:29px;font-size:10.5px}
.btn.wide::before{width:30%}
.footer-band{position:absolute;left:0;bottom:0;width:100%;height:47px;background:var(--footer-band)}
.card{position:absolute;left:14px;width:212px;background:var(--white);border-radius:2px;box-shadow:0 1px 4px rgba(200,90,80,.12)}
.profile-card{height:41px;padding:6px 8px 0 8px}
.profile-card .avatar{position:absolute;left:0;top:-8px;width:20px;height:20px;background:linear-gradient(160deg,#7AA0C8,#3E4A66)}
.profile-card .name{position:absolute;left:24px;top:5px;font-size:7px;font-style:italic;font-weight:500;color:#1a1a1a}
.profile-card .bio{position:absolute;left:7px;top:17px;right:14px;font-size:5.2px;font-style:italic;line-height:1.75;color:#333}
.profile-card .check{position:absolute;right:6px;top:4px;width:7px;height:7px;border:0.6px solid #ddd;background:#fff}
.question-card{height:56px;padding:7px 10px}
.q-num{font-size:8.5px;font-style:italic;font-weight:500;color:#1a1a1a;margin-bottom:2px}
.q-text{font-size:8px;font-style:italic;line-height:12px;color:#222}
.edit-icon{position:absolute;right:5px;top:4px}
.answer-card{height:93px;padding:6px 10px}
.answer-field{position:absolute;left:5px;right:12px;top:60px;height:64px;background:var(--field);border-radius:2px;font-size:5.5px;font-style:italic;color:var(--muted);padding:8px 7px}
.field-label{position:absolute;font-size:8px;font-style:italic;color:#222}
.select{position:absolute;left:145px;top:179px;width:75px;height:17px;background:var(--white);font-size:8.5px;font-style:italic;line-height:17px;padding-left:6px}
.select svg{position:absolute;right:5px;top:6px}
.textarea{position:absolute;left:15px;top:228px;width:209px;height:105px;background:var(--white);border-radius:2px;padding:8px 6px;font-size:7px;font-style:italic;line-height:12px;color:#CFC9C9}
.word-count{position:absolute;left:16px;top:335px;font-size:5px;color:#333}
</style>
</head>
<body>

<!-- Screen: Feedback home -->
<section class="screen" style="left:77px;top:160px">
  <div class="status-bar">9:30<svg class="status-icons" width="24" height="8" viewBox="0 0 24 8"><path d="M0 1h7L3.5 7z" fill="#fff"/><path d="M9 7h6V1z" fill="#fff"/><rect x="18" y="0" width="4" height="8" fill="#fff"/></svg></div>
  <header class="app-bar left-title">Feedback<svg class="nav-action" width="3" height="11" viewBox="0 0 3 11"><circle cx="1.5" cy="1.5" r="1.3" fill="#fff"/><circle cx="1.5" cy="5.5" r="1.3" fill="#fff"/><circle cx="1.5" cy="9.5" r="1.3" fill="#fff"/></svg></header>
  <div class="illustration" role="img" aria-label="Illustration of a woman with a megaphone stepping out of a phone surrounded by rating stars, likes and chat bubbles" style="left:35px;top:68px;width:175px;height:203px;background:radial-gradient(circle,#F7A8A2 0%,#F4C3BC 45%,rgba(252,234,232,0) 72%)"></div>
  <a class="btn" style="left:24px;top:302px;width:110px"><span class="face"></span><span class="label">Request Feedback</span></a>
  <a class="btn right" style="left:96px;top:342px;width:116px"><span class="face"></span><span class="label">Respond to Feedback</span></a>
</section>

<!-- Screen: Request Feedback -->
<section class="screen" style="left:348px;top:160px">
  <div class="status-bar">9:30<svg class="status-icons" width="24" height="8" viewBox="0 0 24 8"><path d="M0 1h7L3.5 7z" fill="#fff"/><path d="M9 7h6V1z" fill="#fff"/><rect x="18" y="0" width="4" height="8" fill="#fff"/></svg></div>
  <header class="app-bar"><svg class="nav-back" width="10" height="9" viewBox="0 0 10 9"><path d="M10 4.5H2M5 1 1.5 4.5 5 8" stroke="#fff" stroke-width="1.4" fill="none"/></svg>Request Feedback</header>
  <div class="illustration" role="img" aria-label="Illustration of two colleagues exchanging review cards with star ratings among leaves" style="left:25px;top:91px;width:194px;height:159px;border-radius:40%;background:radial-gradient(ellipse,#C8C2EE 0%,#F2B6AE 45%,rgba(252,234,232,0) 72%)"></div>
  <a class="btn" style="left:24px;top:275px;width:110px"><span class="face"></span><span class="label">Adhoc Feedback</span></a>
  <a class="btn right" style="left:96px;top:315px;width:116px"><span class="face"></span><span class="label">Mid Year Feedback</span></a>
  <a class="btn" style="left:24px;top:356px;width:110px"><span class="face"></span><span class="label">360 Feedback</span></a>
</section>

<!-- Screen: Request Feedback, adhoc selected -->
<section class="screen" style="left:619px;top:160px">
  <div class="status-bar">9:30<svg class="status-icons" width="24" height="8" viewBox="0 0 24 8"><path d="M0 1h7L3.5 7z" fill="#fff"/><path d="M9 7h6V1z" fill="#fff"/><rect x="18" y="0" width="4" height="8" fill="#fff"/></svg></div>
  <header class="app-bar"><svg class="nav-back" width="10" height="9" viewBox="0 0 10 9"><path d="M10 4.5H2M5 1 1.5 4.5 5 8" stroke="#fff" stroke-width="1.4" fill="none"/></svg>Request Feedback</header>
  <div class="illustration" role="img" aria-label="Illustration of two colleagues exchanging review cards with star ratings among leaves" style="left:25px;top:91px;width:194px;height:159px;border-radius:40%;background:radial-gradient(ellipse,#C8C2EE 0%,#F2B6AE 45%,rgba(252,234,232,0) 72%)"></div>
  <a class="btn dark" style="left:24px;top:275px;width:110px"><span class="face"></span><span class="label">Adhoc Feedback</span></a>
  <a class="btn right" style="left:96px;top:315px;width:116px"><span class="face"></span><span class="label">Mid Year Feedback</span></a>
  <a class="btn" style="left:24px;top:356px;width:110px"><span class="face"></span><span class="label">360 Feedback</span></a>
</section>

<!-- Screen: Select Profile -->
<section class="screen" style="left:889px;top:160px">
  <div class="status-bar">9:30<svg class="status-icons" width="24" height="8" viewBox="0 0 24 8"><path d="M0 1h7L3.5 7z" fill="#fff"/><path d="M9 7h6V1z" fill="#fff"/><rect x="18" y="0" width="4" height="8" fill="#fff"/></svg></div>
  <header class="app-bar"><svg class="nav-back" width="10" height="9" viewBox="0 0 10 9"><path d="M10 4.5H2M5 1 1.5 4.5 5 8" stroke="#fff" stroke-width="1.4" fill="none"/></svg>Select Profile</header>
  <div class="illustration" role="img" aria-label="Illustration of people around a large monitor showing profile cards" style="left:37px;top:59px;width:163px;height:100px;border-radius:30%;background:radial-gradient(ellipse,#E9D9DA 0%,#F3C5C0 45%,rgba(252,234,232,0) 72%)"></div>
  <div class="card profile-card" style="top:181px"><span class="avatar" role="img" aria-label="Profile photo"></span><span class="name">Colin R. Ashby</span><svg class="check" viewBox="0 0 7 7"><path d="M1.5 3.6 3 5 5.6 1.8" stroke="#EC4F4E" stroke-width="0.8" fill="none"/></svg><p class="bio">Lorem ipsum dolor sit amet, consectetur adipiscing elit, sed do eiusmod tempor incididunt ut labore et dolore magna aliqua. Quis ipsum</p></div>
  <div class="card profile-card" style="top:242px"><span class="avatar" role="img" aria-label="Profile photo"></span><span class="name">Martin L. Crowe</span><svg class="check" viewBox="0 0 7 7"><path d="M1.5 3.6 3 5 5.6 1.8" stroke="#EC4F4E" stroke-width="0.8" fill="none"/></svg><p class="bio">Lorem ipsum dolor sit amet, consectetur adipiscing elit, sed do eiusmod tempor incididunt ut labore et dolore magna aliqua. Quis ipsum</p></div>
  <div class="card profile-card" style="top:302px"><span class="avatar" role="img" aria-label="Profile photo"></span><span class="name">Pablo E. Serrat</span><svg class="check" viewBox="0 0 7 7"><path d="M1.5 3.6 3 5 5.6 1.8" stroke="#EC4F4E" stroke-width="0.8" fill="none"/></svg><p class="bio">Lorem ipsum dolor sit amet, consectetur adipiscing elit, sed do eiusmod tempor incididunt ut labore et dolore magna aliqua. Quis ipsum</p></div>
  <div class="card profile-card" style="top:362px"><span class="avatar" role="img" aria-label="Profile photo"></span><span class="name">Oliver T. Hensley</span><svg class="check" viewBox="0 0 7 7"></svg></div>
  <div class="footer-band"></div>
  <a class="btn wide" style="left:22px;top:391px;width:195px"><span class="face"></span><span class="label">Continue</span></a>
</section>

<!-- Screen: Questions -->
<section class="screen" style="left:77px;top:620px">
  <div class="status-bar">9:30<svg class="status-icons" width="24" height="8" viewBox="0 0 24 8"><path d="M0 1h7L3.5 7z" fill="#fff"/><path d="M9 7h6V1z" fill="#fff"/><rect x="18" y="0" width="4" height="8" fill="#fff"/></svg></div>
  <header class="app-bar"><svg class="nav-back" width="10" height="9" viewBox="0 0 10 9"><path d="M10 4.5H2M5 1 1.5 4.5 5 8" stroke="#fff" stroke-width="1.4" fill="none"/></svg>Questions</header>
  <div class="illustration" role="img" aria-label="Illustration of two people beside a large question mark" style="left:62px;top:53px;width:116px;height:97px;border-radius:40%;background:radial-gradient(ellipse,#F08B86 0%,#F4C0B8 45%,rgba(252,234,232,0) 72%)"></div>
  <div class="card question-card" style="top:164px"><svg class="edit-icon" width="7" height="7" viewBox="0 0 7 7"><path d="M5 .5 6.5 2 3 5.5H1.5V4z M.5 6.5h6" stroke="#AAA" stroke-width="0.6" fill="none"/></svg><p class="q-num">01.</p><p class="q-text">It is a long established fact that a reader will be distracted by the readable content of a page when looking at its layout.</p></div>
  <div class="card question-card" style="top:236px"><svg class="edit-icon" width="7" height="7" viewBox="0 0 7 7"><path d="M5 .5 6.5 2 3 5.5H1.5V4z M.5 6.5h6" stroke="#AAA" stroke-width="0.6" fill="none"/></svg><p class="q-num">02.</p><p class="q-text">It is a long established fact that a reader will be distracted by the readable content of a page when looking at its layout.</p></div>
  <div class="card question-card" style="top:308px"><svg class="edit-icon" width="7" height="7" viewBox="0 0 7 7"><path d="M5 .5 6.5 2 3 5.5H1.5V4z M.5 6.5h6" stroke="#AAA" stroke-width="0.6" fill="none"/></svg><p class="q-num">03.</p><p class="q-text">It is a long established fact that a reader will be distracted by the readable content of a page when looking at its layout.</p></div>
  <div class="footer-band"></div>
  <a class="btn wide" style="left:22px;top:390px;width:195px"><span class="face"></span><span class="label">Submit</span></a>
</section>

<!-- Screen: Questions Edit -->
<section class="screen" style="left:348px;top:620px">
  <div class="status-bar">9:30<svg class="status-icons" width="24" height="8" viewBox="0 0 24 8"><path d="M0 1h7L3.5 7z" fill="#fff"/><path d="M9 7h6V1z" fill="#fff"/><rect x="18" y="0" width="4" height="8" fill="#fff"/></svg></div>
  <header class="app-bar"><svg class="nav-back" width="10" height="9" viewBox="0 0 10 9"><path d="M10 4.5H2M5 1 1.5 4.5 5 8" stroke="#fff" stroke-width="1.4" fill="none"/></svg>Questions Edit</header>
  <div class="illustration" role="img" aria-label="Illustration of two people beside a large question mark" style="left:62px;top:53px;width:116px;height:97px;border-radius:40%;background:radial-gradient(ellipse,#F08B86 0%,#F4C0B8 45%,rgba(252,234,232,0) 72%)"></div>
  <span class="field-label" style="left:25px;top:183px">Questions No.</span>
  <div class="select">01<svg width="6" height="4" viewBox="0 0 6 4"><path d="M.5.5 3 3 5.5.5" stroke="#333" stroke-width="0.9" fill="none"/></svg></div>
  <span class="field-label" style="left:25px;top:212px">Questions Editing</span>
  <svg style="position:absolute;left:216px;top:213px" width="8" height="8" viewBox="0 0 7 7"><path d="M5 .5 6.5 2 3 5.5H1.5V4z M.5 6.5h6" stroke="#AAA" stroke-width="0.6" fill="none"/></svg>
  <div class="textarea">It is a long established fact that a reader will be distracted by the readable content of a page when looking at its layout.</div>
  <span class="word-count">Word Count 100</span>
  <div class="footer-band"></div>
  <a class="btn wide" style="left:22px;top:390px;width:195px"><span class="face"></span><span class="label">Update</span></a>
</section>

<!-- Screen: Answer -->
<section class="screen" style="left:619px;top:620px">
  <div class="status-bar">9:30<svg class="status-icons" width="24" height="8" viewBox="0 0 24 8"><path d="M0 1h7L3.5 7z" fill="#fff"/><path d="M9 7h6V1z" fill="#fff"/><rect x="18" y="0" width="4" height="8" fill="#fff"/></svg></div>
  <header class="app-bar"><svg class="nav-back" width="10" height="9" viewBox="0 0 10 9"><path d="M10 4.5H2M5 1 1.5 4.5 5 8" stroke="#fff" stroke-width="1.4" fill="none"/></svg>Answer<svg class="nav-action" width="10" height="11" viewBox="0 0 10 11"><path d="M5 1C3 1 2 2.6 2 4.5V7L1 8.3h8L8 7V4.5C8 2.6 7 1 5 1z" fill="#fff"/><circle cx="5" cy="9.6" r="1.1" fill="#fff"/></svg></header>
  <div class="card answer-card" style="top:56px"><p class="q-num">01.</p><p class="q-text">It is a long established fact that a reader will be distracted by the readable content of a page when looking at its layout.</p><div class="answer-field">Enter Your Answer</div></div>
  <div class="card answer-card" style="top:193px"><p class="q-num">02.</p><p class="q-text">The point of using Lorem Ipsum is that it has a more-or-less normal distribution of letters, as opposed to using ‘Content here, content here’</p><div class="answer-field">Enter Your Answer</div></div>
  <div class="card answer-card" style="top:330px"><p class="q-num">03.</p><p class="q-text">Many desktop publishing packages and web page editors now use Lorem Ipsum as their default model text.</p></div>
  <div class="footer-band"></div>
  <a class="btn wide" style="left:22px;top:390px;width:195px"><span class="face"></span><span class="label">Update</span></a>
</section>

</body>
</html>
```